Bright Towns Alliance PowerPoint Design Template and Sample Deck

The Bright Towns Alliance is an international organization that seeks to improve the livability, workability and sustainability of the world’s cities.
We seek a versatile PowerPoint design template with 10 slide types plus a “self-documenting” sample deck. Your design will be used in keynote speeches and workshops around the world.
After the contest is completed, we will ask the winning designer to add 10-20 additional slide types for $75 per slide. We also seek a long-term relationship whereby we can request “custom” slides and/or ask the designer to touch up the slides we build to make them better.
FILES. We have uploaded several files:
2. PALETTE. Shows our official colors.
3 LOGOS. Several individual files with different variations of our logo. Some with our motto, some without.
2. SAMPLE SLIDES. Because we were unable to successfully upload our sample deck, we are making it available via this FileCrate link:
https://www.filecrate-example.net/s/q7mrk2tzw9hdn4e/The%20Bright%20Towns%20Alliance%20Design%20Contest%20Notes.docx?dl=0
Target Market(s)
Mayors, department heads, CIOs, senior executives from technology companies
Industry/Entity Type
Information Technology
Colors
Designer to choose colors to be used in the design.
Requirements
Must have
- Please see uploaded Word document for requirements, nice to haves and should not haves and uploaded palette for color preferences.
Nice to have
- see above
Should not have
- see above

```html
<!DOCTYPE html>
<html lang="en">
<head>
<meta charset="utf-8">
<title>Bright Towns Alliance – Slide Template</title>
<link rel="stylesheet" href="https://fonts.googleapis.com/css2?family=Lato:wght@400;700&family=Anton&family=Oswald:wght@400&family=Arimo:wght@400;700&display=swap">
<style>
  :root{
    --orange:#f5841f;
    --navy:#1b2f5e;
    --band-blue:#5b86c8;
    --quote-blue:#1d4f91;
    --red:#e31b1b;
    --ink:#222;
    --paper:#f7f7f7;
    --stage:#ececec;
    --tab:#141414;
  }
  *{box-sizing:border-box;margin:0;padding:0}
  html,body{width:1200px;height:922px;overflow:hidden}
  body{background:radial-gradient(ellipse at center,#fafafa 0%,var(--stage) 100%);font-family:"Arimo",Arial,sans-serif;position:relative}

  .slide{position:absolute;width:571px;height:402px;background:linear-gradient(#ffffff,var(--paper));box-shadow:0 2px 6px rgba(0,0,0,.35);overflow:hidden}
  .slide--1{left:22px;top:20px}
  .slide--2{left:611px;top:20px}
  .slide--3{left:22px;top:476px}
  .slide--4{left:611px;top:476px}

  .caption{position:absolute;width:571px;text-align:center;font-size:16px;color:var(--ink);letter-spacing:.3px}
  .caption--1{left:22px;top:433px}
  .caption--2{left:611px;top:433px}
  .caption--3{left:22px;top:890px}
  .caption--4{left:611px;top:890px}

  .brand{position:absolute;left:0;width:100%;text-align:center;font-family:"Lato",sans-serif;font-weight:400;color:var(--navy);white-space:nowrap}
  .brand--large{top:18px;font-size:32px;line-height:38px}
  .brand--small{top:18px;font-size:25px;line-height:30px}

  .headline{position:absolute;left:0;width:100%;text-align:center;font-family:"Anton",sans-serif;color:var(--orange);font-size:34px;line-height:40px;top:68px;letter-spacing:.5px}
  .rule{position:absolute;left:0;width:100%;height:3px;background:var(--orange)}

  .photo{position:absolute}
  .photo--towers{left:0;top:118px;width:571px;height:260px;background:linear-gradient(100deg,#1f3d78 0%,#4c73b5 35%,#2a4c8c 55%,#6f93cc 80%,#2c5196 100%)}
  .photo--desk{left:0;top:126px;width:571px;height:122px;background:linear-gradient(90deg,#3a3a3c 0%,#7a6552 45%,#a88a68 70%,#d9d6d2 100%)}
  .photo--laptop{left:0;top:254px;width:571px;height:124px;background:linear-gradient(90deg,#c9c2b8 0%,#8a7a66 30%,#e6e4e0 55%,#b9a98f 80%,#3d4e6a 100%)}
  .photo--phone{left:0;top:76px;width:571px;height:298px;background:linear-gradient(160deg,#8a7060 0%,#3c4a66 40%,#1f2b48 70%,#7a6a5a 100%)}
  .photo--workspace{left:0;top:76px;width:246px;height:298px;background:linear-gradient(170deg,#5a4a40 0%,#333536 50%,#5c5750 100%)}

  .frame{position:absolute;border:1px solid rgba(255,255,255,.85)}

  .tabs{position:absolute;left:6px;top:332px;display:flex;gap:8px}
  .tab{position:relative;width:86px;height:29px;background:var(--tab);color:#fff;font-size:10.5px;line-height:29px;text-align:center}
  .tab--active::after{content:"";position:absolute;left:34px;bottom:-10px;border-left:10px solid transparent;border-right:10px solid transparent;border-top:10px solid var(--tab)}

  .title-band{position:absolute;left:0;top:62px;width:571px;height:58px;background:var(--band-blue);color:#fff;font-family:"Anton",sans-serif;font-size:42px;line-height:58px;text-align:center;letter-spacing:.5px;font-weight:400}

  .footer{position:absolute;left:0;top:380px;width:571px;height:22px}
  .footer svg{position:absolute;left:0;top:0}
  .footer__url{position:absolute;left:130px;right:44px;top:5px;text-align:center;font-size:9.5px;font-weight:700;color:#111}
  .footer__num{position:absolute;right:0;top:2px;width:44px;height:20px;background:#0c0c0c;color:#fff;font-size:9.5px;font-weight:700;text-align:center;line-height:20px}

  .quote{position:absolute;left:0;top:173px;width:356px;height:144px;background:var(--quote-blue)}
  .quote__mark{font-family:"Anton",sans-serif;color:var(--orange)}
  .quote__mark--open{position:absolute;left:11px;top:8px;font-size:40px;line-height:40px}
  .quote__mark--close{font-size:30px;line-height:10px;vertical-align:-12px;margin-left:6px}
  .quote__text{position:absolute;left:40px;top:19px;width:292px;font-family:"Oswald",sans-serif;color:#fff;font-size:17px;line-height:23.3px}
  .quote__source{position:absolute;left:40px;top:120px;color:#fff;font-size:9px;font-weight:700;font-style:normal}

  .overlay-title{position:absolute;left:39px;top:192px;font-family:"Anton",sans-serif;font-size:28px;line-height:33px;font-weight:400}
  .overlay-title__accent{color:var(--red);display:block}
  .overlay-title__rest{color:#fff;display:block}

  .section{position:absolute;left:258px;width:300px}
  .section--1{top:88px}
  .section--2{top:198px}
  .section__head{position:relative;height:22px}
  .section__num{position:absolute;left:0;top:0;width:22px;height:22px;border:2px solid var(--navy);border-radius:50%;background:#fff;color:var(--navy);font-weight:700;font-size:13px;line-height:18px;text-align:center;z-index:1}
  .section__bar{position:absolute;left:12px;top:2px;width:144px;height:18px;background:var(--navy);clip-path:polygon(0 0,92% 0,100% 100%,0 100%);color:#fff;font-size:12.5px;line-height:18px;padding-left:29px}
  .section__body{margin:8px 0 0 27px;width:266px;font-size:6.5px;line-height:10px;color:#333;text-align:justify}

  .checklist{position:absolute;left:285px;top:301px;list-style:none}
  .checklist li{font-size:6.8px;line-height:10px;color:#333;padding-left:10px;position:relative}
  .checklist svg{position:absolute;left:0;top:2px}
</style>
</head>
<body>

<section class="slide slide--1">
  <div class="brand brand--large">Bright Towns Alliance</div>
  <h1 class="headline">PROGRESSIVE AGENDA</h1>
  <div class="rule" style="top:115px"></div>
  <div class="photo photo--towers" role="img" aria-label="Photo of blue glass office towers seen from below"></div>
  <nav class="tabs">
    <div class="tab tab--active">LOREM IPSUM</div>
    <div class="tab">LOREM IPSUM</div>
    <div class="tab">LOREM IPSUM</div>
    <div class="tab">LOREM IPSUM</div>
    <div class="tab">LOREM IPSUM</div>
    <div class="tab">LOREM IPSUM</div>
  </nav>
  <footer class="footer">
    <svg width="571" height="22" viewBox="0 0 571 22"><polygon points="0,19 118,19 134,2 527,2 527,22 0,22" fill="var(--orange)"/></svg>
    <div class="footer__url">www.websiteaddress.com</div>
    <div class="footer__num">01</div>
  </footer>
</section>
<div class="caption caption--1">SLIDER 1</div>

<section class="slide slide--2">
  <div class="brand brand--small">Bright Towns Alliance</div>
  <h1 class="title-band">LOREM IPSUM DOLOR SIT</h1>
  <div class="photo photo--desk" role="img" aria-label="Photo of hands typing on a laptop beside a newspaper at a wooden table"></div>
  <div class="frame" style="left:11px;top:138px;width:548px;height:98px"></div>
  <div class="photo photo--laptop" role="img" aria-label="Photo of an open laptop on a desk with a copper cup and notebooks"></div>
  <div class="frame" style="left:11px;top:268px;width:548px;height:96px"></div>
  <footer class="footer">
    <svg width="571" height="22" viewBox="0 0 571 22"><polygon points="0,19 118,19 134,2 527,2 527,22 0,22" fill="var(--orange)"/></svg>
    <div class="footer__url">www.websiteaddress.com</div>
    <div class="footer__num">02</div>
  </footer>
</section>
<div class="caption caption--2">SLIDER 2</div>

<section class="slide slide--3">
  <div class="brand brand--large">Bright Towns Alliance</div>
  <div class="rule" style="top:73px"></div>
  <div class="photo photo--phone" role="img" aria-label="Photo of hands holding a smartphone above a laptop"></div>
  <blockquote class="quote">
    <span class="quote__mark quote__mark--open">“</span>
    <p class="quote__text">Lorem Ipsum is simply dummy text of the printing and typesetting industry. Lorem Ipsum has been the industry's standard dummy text ever since the 1500s.<span class="quote__mark quote__mark--close">”</span></p>
    <cite class="quote__source">- LOREM IPSUM DOLOR -</cite>
  </blockquote>
  <footer class="footer">
    <svg width="571" height="22" viewBox="0 0 571 22"><polygon points="0,19 118,19 134,2 527,2 527,22 0,22" fill="var(--orange)"/></svg>
    <div class="footer__url">www.websiteaddress.com</div>
    <div class="footer__num">03</div>
  </footer>
</section>
<div class="caption caption--3">SLIDER 3</div>

<section class="slide slide--4">
  <div class="brand brand--small">Bright Towns Alliance</div>
  <div class="photo photo--workspace" role="img" aria-label="Photo of a laptop, a phone and a potted plant on a desk"></div>
  <h2 class="overlay-title"><span class="overlay-title__accent">LOREM</span><span class="overlay-title__rest">IPSUM DOLOR</span></h2>

  <div class="section section--1">
    <div class="section__head"><div class="section__num">1</div><div class="section__bar">LOREM IPSUM</div></div>
    <p class="section__body">Lorem Ipsum is simply dummy text of the printing and typesetting industry. Lorem Ipsum has been the industry's standard dummy text ever since the 1500s, when an unknown printer took a galley of type and scrambled it to make a type specimen book. It has survived not only five centuries, but also the leap into electronic typesetting, remaining essentially unchanged. It was popularised in the 1960s with the release of Letraset sheets containing Lorem Ipsum passages, and more recently with desktop publishing software.</p>
  </div>
  <div class="section section--2">
    <div class="section__head"><div class="section__num">2</div><div class="section__bar">LOREM IPSUM</div></div>
    <p class="section__body">Lorem Ipsum is simply dummy text of the printing and typesetting industry. Lorem Ipsum has been the industry's standard dummy text ever since the 1500s, when an unknown printer took a galley of type and scrambled it to make a type specimen book. It has survived not only five centuries, but also the leap into electronic typesetting, remaining essentially unchanged. It was popularised in the 1960s with the release of Letraset sheets containing Lorem Ipsum passages, and more recently with desktop publishing software.</p>
  </div>
  <ul class="checklist">
    <li><svg width="7" height="7" viewBox="0 0 10 10"><circle cx="5" cy="5" r="4" fill="none" stroke="var(--orange)" stroke-width="1.3"/><path d="M3 5l1.5 1.5L8 3" fill="none" stroke="var(--orange)" stroke-width="1.3"/></svg>Lorem Ipsum is simply dummy text</li>
    <li><svg width="7" height="7" viewBox="0 0 10 10"><circle cx="5" cy="5" r="4" fill="none" stroke="var(--orange)" stroke-width="1.3"/><path d="M3 5l1.5 1.5L8 3" fill="none" stroke="var(--orange)" stroke-width="1.3"/></svg>Lorem Ipsum is simply dummy text</li>
    <li><svg width="7" height="7" viewBox="0 0 10 10"><circle cx="5" cy="5" r="4" fill="none" stroke="var(--orange)" stroke-width="1.3"/><path d="M3 5l1.5 1.5L8 3" fill="none" stroke="var(--orange)" stroke-width="1.3"/></svg>Lorem Ipsum is simply dummy text</li>
    <li><svg width="7" height="7" viewBox="0 0 10 10"><circle cx="5" cy="5" r="4" fill="none" stroke="var(--orange)" stroke-width="1.3"/><path d="M3 5l1.5 1.5L8 3" fill="none" stroke="var(--orange)" stroke-width="1.3"/></svg>Lorem Ipsum is simply dummy text</li>
  </ul>
  <footer class="footer">
    <svg width="571" height="22" viewBox="0 0 571 22"><polygon points="0,19 118,19 134,2 527,2 527,22 0,22" fill="var(--orange)"/></svg>
    <div class="footer__url">www.websiteaddress.com</div>
    <div class="footer__num">04</div>
  </footer>
</section>
<div class="caption caption--4">SLIDER 4</div>

</body>
</html>
```